Volora Laundry and Dry Cleaning Poster

We need a Poster and Window Sticker for our Laundry and Dry cleaning shop (VOLORA LAUNDRY AND DRY CLEANING).
info we like on the design. Logo is included
Company Name: Volora Laundry and Dry Cleaning
Slogan: It Comes Back Clean
Location: Kwentu-Dasor, Accra
Working Hours: Mon-Sat 8am to 5pm
Tel: +233 30 781 6242
email:info@voloralaundry.example
website: www.voloralaundry.example
fb: fb.com/voloralaundry

Target Market(s)

Laundry Shop

Colors
33a6d7
9bcb3b

```html
<!DOCTYPE html>
<html lang="en">
<head>
<meta charset="utf-8">
<title>Volora Laundry and Dry Cleaning Poster</title>
<link rel="stylesheet" href="https://fonts.googleapis.com/css2?family=Fredoka:wght@600;700&family=Alfa+Slab+One&family=Baloo+2:wght@700&display=swap">
<style>
  :root {
    --blue: #1f9ad6;
    --blue-deep: #1e86c8;
    --teal: #27b8a2;
    --teal-dark: #1f9c89;
    --paper: #f9f9fb;
    --grey: #efefef;
    --ink: #0b0b0b;
    --white: #ffffff;
  }
  * { margin: 0; padding: 0; box-sizing: border-box; }
  html, body { width: 1200px; height: 960px; overflow: hidden; background: var(--grey); }
  .poster { position: relative; width: 1200px; height: 960px; overflow: hidden; }
  .backdrop { position: absolute; inset: 0; }

  .brand { position: absolute; left: 44px; top: 40px; display: flex; align-items: center; gap: 18px; }
  .brand-dot { width: 200px; height: 200px; border-radius: 50%; background: var(--blue); }
  .brand-name { font-family: "Fredoka", sans-serif; font-weight: 600; color: var(--blue); line-height: 1; }
  .brand-name .word { display: block; font-size: 128px; letter-spacing: 2px; }
  .brand-name .line { display: block; font-size: 25px; margin-top: 8px; letter-spacing: 0.5px; }

  .sparkle { position: absolute; left: 796px; top: 130px; width: 370px; height: 200px;
    background: radial-gradient(ellipse at 75% 55%, rgba(39,184,162,0.55), rgba(39,184,162,0.08) 70%, transparent 75%); }

  .slogan { position: absolute; left: 306px; top: 236px; font-family: "Fredoka", sans-serif; font-weight: 700;
    font-size: 76px; color: var(--teal); letter-spacing: -0.5px; }

  .service-art { position: absolute; }
  .service-art.wash { left: 130px; top: 456px; width: 200px; height: 180px; background: linear-gradient(135deg, #e4e6ea, #4fc1ea); border-radius: 10px; }
  .service-art.dry { left: 496px; top: 376px; width: 210px; height: 200px; background: linear-gradient(90deg, #1a3a8f, #f7cf1e 50%, #5b5b5b); border-radius: 10px; opacity: 0.85; }
  .service-art.press { left: 862px; top: 440px; width: 200px; height: 190px; background: linear-gradient(135deg, #e9ebef, #22c28f); border-radius: 10px; }

  .hours { position: absolute; left: 0; width: 1200px; text-align: center; }
  .hours-title { top: 668px; left: -10px; font-family: "Fredoka", sans-serif; font-weight: 700; font-size: 54px; color: var(--ink); }
  .hours-time { top: 724px; left: 28px; font-family: "Alfa Slab One", serif; font-size: 56px; letter-spacing: 1px;
    text-shadow: 3px 3px 0 #1b3b4a; }
  .hours-time .days { color: var(--blue); }
  .hours-time .span { color: var(--teal); }

  .contact { position: absolute; font-family: "Baloo 2", sans-serif; font-weight: 700; color: var(--white); white-space: nowrap; line-height: 1; }
  .contact.phone { left: 524px; top: 862px; font-size: 26px; }
  .contact.social { left: 996px; top: 862px; font-size: 26px; }
  .contact.address { left: 28px; top: 916px; font-size: 25px; }
  .contact.web { left: 396px; top: 918px; font-size: 24px; }
  .contact.mail { left: 846px; top: 918px; font-size: 23px; }
  .at-sign { position: absolute; left: 346px; top: 904px; transform: translate(-50%, -54%);
    font-family: "Baloo 2", sans-serif; font-weight: 700; font-size: 40px; color: var(--white); }
</style>
</head>
<body>
<main class="poster">
  <svg class="backdrop" width="1200" height="960" viewBox="0 0 1200 960" aria-hidden="true">
    <rect width="1200" height="960" fill="var(--grey)"/>
    <ellipse class="arc-teal" cx="600" cy="136" rx="740" ry="520" fill="var(--teal)"/>
    <ellipse class="arc-blue" cx="600" cy="93" rx="720" ry="483" fill="var(--blue)"/>
    <ellipse class="arc-paper" cx="600" cy="-33" rx="700" ry="561" fill="var(--paper)"/>

    <g class="hex-frames">
      <polygon points="60,546 148,404 328,404 416,546 328,688 148,688" fill="var(--teal)"/>
      <polygon points="74,546 155,415 321,415 402,546 321,677 155,677" fill="var(--blue-deep)"/>
      <polygon points="82,546 160,422 316,422 394,546 316,670 160,670" fill="var(--teal)"/>
      <polygon points="90,546 165,430 311,430 386,546 311,662 165,662" fill="var(--paper)"/>

      <polygon points="424,488 512,352 688,352 776,488 688,624 512,624" fill="var(--teal)"/>
      <polygon points="438,488 519,363 681,363 762,488 681,613 519,613" fill="var(--blue-deep)"/>
      <polygon points="446,488 524,370 676,370 754,488 676,606 524,606" fill="var(--teal)"/>
      <polygon points="454,488 529,378 671,378 746,488 671,598 529,598" fill="var(--paper)"/>

      <polygon points="784,546 872,404 1048,404 1136,546 1048,688 872,688" fill="var(--teal)"/>
      <polygon points="798,546 879,415 1041,415 1122,546 1041,677 879,677" fill="var(--blue-deep)"/>
      <polygon points="806,546 884,422 1036,422 1114,546 1036,670 884,670" fill="var(--teal)"/>
      <polygon points="814,546 889,430 1031,430 1106,546 1031,662 889,662" fill="var(--paper)"/>
    </g>

    <g class="footer-bands">
      <rect x="0" y="850" width="1200" height="56" fill="var(--blue-deep)"/>
      <rect x="0" y="904" width="1200" height="56" fill="var(--teal)"/>
      <circle cx="148" cy="858" r="36" fill="var(--blue-deep)"/>
      <circle cx="466" cy="858" r="36" fill="var(--blue-deep)"/>
      <circle cx="938" cy="858" r="36" fill="var(--blue-deep)"/>
      <circle cx="346" cy="904" r="36" fill="var(--teal)"/>
      <circle cx="800" cy="904" r="36" fill="var(--teal)"/>
    </g>

    <g class="icon-pin" fill="var(--white)">
      <path d="M148 832c-10 0-18 8-18 18 0 13 18 30 18 30s18-17 18-30c0-10-8-18-18-18zm0 25a7 7 0 1 1 0-14 7 7 0 0 1 0 14z"/>
      <ellipse cx="148" cy="884" rx="18" ry="5" fill="none" stroke="var(--white)" stroke-width="3"/>
    </g>
    <path class="icon-phone" fill="var(--white)" d="M451 840c3-3 7-3 9 0l5 7c2 3 1 6-1 8l-3 3c2 5 7 10 12 12l3-3c2-2 5-3 8-1l7 5c3 2 3 6 0 9l-4 4c-4 4-14 1-24-9s-13-20-9-24z"/>
    <g class="icon-mail" fill="none" stroke="var(--white)" stroke-width="3">
      <rect x="781" y="891" width="38" height="26" rx="2" fill="var(--white)"/>
      <path d="M781 891l19 15 19-15" stroke="var(--teal)"/>
    </g>
  </svg>

  <div class="brand">
    <span class="brand-dot" aria-hidden="true"></span>
    <p class="brand-name"><span class="word">Volora</span><span class="line">LAUNDRY AND DRY CLEANING</span></p>
  </div>

  <div class="sparkle" role="img" aria-label="Trail of teal stars growing in size"></div>

  <h1 class="slogan">It Comes Back Clean</h1>

  <div class="service-art wash" role="img" aria-label="Attendant loading stacked washing machines"></div>
  <div class="service-art dry" role="img" aria-label="Dry-cleaned dresses and jacket hanging in garment bags"></div>
  <div class="service-art press" role="img" aria-label="Steam iron beside a green top on a hanger"></div>

  <h2 class="hours hours-title">Working Hours</h2>
  <p class="hours hours-time"><span class="days">Mon-Sat</span>&nbsp; <span class="span">8am to 5pm</span></p>

  <span class="at-sign" aria-hidden="true">@</span>
  <p class="contact phone">+233 30 781 6242</p>
  <p class="contact social">Voloralaundry</p>
  <p class="contact address">Kwentu-Dasor, Accra</p>
  <p class="contact web">www.voloralaundry.example</p>
  <p class="contact mail">info@voloralaundry.example</p>
</main>
</body>
</html>
```